Page hosted on godaddy.com, Website domain is dalworth4kiva.com

Page should be based on design of my campaign flyer. I will put all text inside pages, they can be layout with top navigation and bottom header that contains contact information. Pages should be white background

I will use html to edit, or I can also get an editor if you specify which one your design is compatible with

Items listed below that are underlined are actual HTML pages
Total number of pages (including BLOG) = 18

Site Structure

HOME
Blog – should be a wordpress blog inside this page
KIVA Board
• Why I am running
• About Me
• How to vote
Automotive
• My Automotive Career
• Automotive for Fun
• Specialty car brokerage
Aviation
• Aviation Experience
• My Favorite Aviation Projects
• Aviation Sales Business
Other Experience
• My Complete Timeline
• Entrepreneurial Activities
• Dalworth Orchard
• Commercial Development
• Home Construction
• Education
Photos
Updates

update, I would ideally like to use wordpress for the site design.

```html
<!DOCTYPE html>
<html lang="en">
<head>
<meta charset="utf-8">
<title>Dalworth for KIVA</title>
<link href="https://fonts.googleapis.com/css2?family=Audiowide&family=Roboto:wght@400;500;700&display=swap" rel="stylesheet">
<style>
:root{
  --red:#c41e24;
  --red-dark:#a3161b;
  --ink:#4a4a4a;
  --ink-dark:#2b2b2b;
  --text:#555;
  --white:#fff;
}
*{box-sizing:border-box;margin:0;padding:0}
html,body{width:1200px;height:3708px;overflow:hidden;background:var(--white)}
body{font-family:"Roboto",Arial,sans-serif;color:var(--text)}
.page{position:relative;width:1200px;height:3708px;overflow:hidden;background:var(--white)}
.abs{position:absolute}
.display{font-family:"Audiowide",Arial,sans-serif;text-transform:uppercase}

/* header */
.hero-bg{left:0;top:0;width:1200px;height:900px;background:radial-gradient(ellipse at 60% 40%,#fafafa 0%,#ececec 55%,#dedede 100%)}
.contact-bar{top:0;left:0;width:1200px;height:47px}
.contact-bar-text{top:0;left:672px;height:47px;display:flex;align-items:center;gap:36px;color:var(--white);font-size:14px}
.contact-bar-text span{display:flex;align-items:center;gap:8px}
.brand{font-family:"Audiowide",Arial,sans-serif;color:var(--ink);line-height:1;text-align:center}
.brand .line1{font-size:24px;letter-spacing:1px}
.brand .line2{font-size:18px;letter-spacing:1px;margin-top:4px}
.brand-header{left:69px;top:30px;width:170px}
.nav{display:flex;font-family:"Audiowide",Arial,sans-serif;font-size:15px;text-transform:uppercase;color:var(--ink-dark);white-space:nowrap}
.nav a{color:inherit;text-decoration:none}
.nav a.active{color:var(--red)}
.nav-header{top:82px;left:327px;gap:27px}
.hero-title{left:114px;top:248px;font-size:40px;line-height:44px;color:#5a5a5a;letter-spacing:1px}
.btn{display:flex;align-items:center;justify-content:center;background:var(--red);color:var(--white);font-family:"Audiowide",Arial,sans-serif;text-transform:uppercase;text-decoration:none}
.btn-quote{left:117px;top:443px;width:234px;height:62px;font-size:18px}
.btn-small{width:135px;height:44px;font-size:11px}
.portrait{left:655px;top:187px;width:490px;height:600px;border-radius:240px 240px 0 0;background:linear-gradient(180deg,#caa08a 0%,#8fa8cf 45%,#2a2d36 70%,#1d2027 100%)}
.hero-curves{left:0;top:560px}

/* intro */
.section-title{font-size:35px;line-height:38px;color:#555;letter-spacing:1px}
.intro-title{left:104px;top:896px}
.body-copy{font-size:13px;line-height:17.3px;color:#555}
.body-copy p+p{margin-top:17px}
.intro-copy{left:104px;top:1032px;width:476px}
.intro-btn{left:102px;top:1331px}
.hex-photo{left:616px;top:839px}

/* board */
.board-bg{left:0;top:1400px}
.board-photo{left:94px;top:1724px;width:412px;height:412px;border-radius:50%;background:radial-gradient(circle at 50% 35%,#e02a2a 0%,#b3121a 45%,#3a2a2a 80%,#1a1a1a 100%)}
.board-title{left:547px;top:1758px;font-size:40px}
.board-copy{left:547px;top:1816px;width:430px}
.board-btn{left:547px;top:2061px}

/* blog */
.blog-title{left:0;top:2462px;width:1200px;text-align:center;font-size:42px;color:#555;letter-spacing:1px}
.blog-title .accent{color:var(--red)}
.blog-feature{left:102px;top:2561px;width:451px;height:567px;background:linear-gradient(180deg,#6b5a3a 0%,#2f2c2a 35%,#3d4656 70%,#1c1d22 100%)}
.post-thumb{left:576px;width:215px;height:176px}
.thumb-1{top:2561px;background:linear-gradient(160deg,#5f6670,#2c3036)}
.thumb-2{top:2756px;background:linear-gradient(160deg,#d8dde3,#6d6a68 60%,#3a3b40)}
.thumb-3{top:2950px;background:linear-gradient(180deg,#8fb3d9 0%,#c9d6e2 50%,#7b7b70 100%)}
.post-text{left:823px;width:260px}
.post-date{color:var(--red);font-size:15px;font-weight:500}
.post-heading{margin-top:10px;font-size:18px;line-height:23px;font-weight:500;color:var(--ink-dark)}
.post-excerpt{margin-top:12px;font-size:10px;line-height:13.5px;color:#666}

/* footer */
.footer-shape{left:0;top:3180px}
.badge{left:859px;top:3194px}
.brand-footer{left:518px;top:3396px;width:164px}
.nav-footer{top:3526px;left:0;width:1200px;justify-content:center;gap:26px;font-size:15px}
.contact-pill{left:335px;top:3572px;width:528px;height:52px;border-radius:26px;background:var(--white);display:flex;align-items:center;justify-content:center;gap:38px;font-size:14px;color:var(--ink-dark)}
.contact-pill span{display:flex;align-items:center;gap:8px}
.copyright{left:0;top:3644px;width:1200px;text-align:center;font-size:15px;color:#444}
</style>
</head>
<body>
<div class="page">

  <!-- header / hero -->
  <div class="abs hero-bg"></div>
  <div class="abs portrait" role="img" aria-label="Portrait photograph of the candidate in a dark suit and blue tie"></div>
  <svg class="abs hero-curves" width="1200" height="340" viewBox="0 0 1200 340" aria-hidden="true">
    <path d="M0 80 C300 230 700 150 1200 280 L1200 340 L0 340 Z" fill="#fff"/>
    <path d="M0 60 C300 200 700 120 1200 240 L1200 280 C700 150 300 230 0 80 Z" fill="var(--red)"/>
  </svg>

  <svg class="abs contact-bar" width="1200" height="47" viewBox="0 0 1200 47" aria-hidden="true">
    <path d="M650 0 H1200 V47 H633 Z" fill="var(--red)"/>
  </svg>
  <div class="abs contact-bar-text">
    <span><svg width="15" height="11" viewBox="0 0 15 11"><rect width="15" height="11" rx="1" fill="#fff"/><path d="M0 1 L7.5 6.5 L15 1" stroke="var(--red)" stroke-width="1.5" fill="none"/></svg>alex.dalworth@northmarkdx.com</span>
    <span><svg width="14" height="14" viewBox="0 0 24 24"><path d="M6.6 10.8a15 15 0 0 0 6.6 6.6l2.2-2.2a1 1 0 0 1 1-.3 11 11 0 0 0 3.6.6 1 1 0 0 1 1 1V20a1 1 0 0 1-1 1A17 17 0 0 1 3 4a1 1 0 0 1 1-1h3.5a1 1 0 0 1 1 1 11 11 0 0 0 .6 3.6 1 1 0 0 1-.3 1Z" fill="#fff"/></svg>Phone: (555)XXX-XXXX</span>
  </div>

  <div class="abs brand brand-header"><div class="line1">DALWORTH</div><div class="line2">FOR KIVA</div></div>

  <nav class="abs nav nav-header">
    <a class="active" href="#">Home</a>
    <a href="#">KIVA Board</a>
    <a href="#">Automotive</a>
    <a href="#">Aviation</a>
    <a href="#">Other Experiences</a>
    <a href="#">Photos</a>
  </nav>

  <h1 class="abs display hero-title">I need 30 seconds<br>of your time.<br>I promise it's<br>important</h1>
  <a class="abs btn btn-quote" href="#">Get a quote</a>

  <!-- intro -->
  <h2 class="abs display section-title intro-title">New cars are<br>not designed with<br>modification in mind</h2>
  <div class="abs body-copy intro-copy">
    <p>You are probably aware that some autonomous vehicle technology is showing up as features in cars today and will be mainstream soon. This technology is called ADAS, or Advanced Driver Assist Systems. What you may not know is that ADAS systems can malfunction when vehicles are modified. This affects racing, wheels and tires, body modifications, paint (yes, increasing paint thickness on a bumper can cause these systems to read distances wrong), interior changes, and so much more.</p>
    <p>If we don't get in front of ADAS as an aftermarket industry, vehicle customization will impact driver safety and we can expect government regulation preventing modification and customization. I can't stand to the side and watch this happen. I love performance cars, racing, vehicle modification, and customization. I managed Velqor Tuning, am president today of Northmark DX with nearly 400 employees, have an RDRA license, and live the automotive aftermarket.</p>
  </div>
  <a class="abs btn btn-small intro-btn" href="#">Read more</a>

  <svg class="abs hex-photo" width="505" height="576" viewBox="0 0 505 576" role="img" aria-label="Photograph of a red sports sedan parked on grass">
    <defs>
      <linearGradient id="hexFill" x1="0" y1="0" x2="0" y2="1">
        <stop offset="0" stop-color="#c7cfa0"/>
        <stop offset="0.3" stop-color="#8a2029"/>
        <stop offset="0.65" stop-color="#6b141b"/>
        <stop offset="1" stop-color="#4d7a2c"/>
      </linearGradient>
    </defs>
    <polygon points="252,0 505,144 505,432 252,576 0,432 0,144" fill="url(#hexFill)"/>
  </svg>

  <!-- board -->
  <svg class="abs board-bg" width="1200" height="970" viewBox="0 0 1200 970" aria-hidden="true">
    <defs>
      <linearGradient id="boardFill" x1="0" y1="0" x2="1" y2="1">
        <stop offset="0" stop-color="#eae9eb"/>
        <stop offset="0.5" stop-color="#f5f4f5"/>
        <stop offset="1" stop-color="#e6e5e7"/>
      </linearGradient>
    </defs>
    <path d="M0 75 C300 120 600 240 1200 25 L1200 887 L0 960 Z" fill="url(#boardFill)"/>
    <path d="M690 204 L924 204 L868 238 Z" fill="var(--red)"/>
    <path d="M338 840 L420 810 L690 810 L690 815 Z" fill="var(--red)"/>
  </svg>
  <div class="abs board-photo" role="img" aria-label="Photograph of the candidate speaking at a podium on a red-lit stage"></div>
  <h2 class="abs display section-title board-title">KIVA Board</h2>
  <div class="abs body-copy board-copy">
    <p>Lorem ipsum dolor sit amet, consectetur adipiscing elit, sed do eiusmod tempor incididunt ut labore et dolore magna aliqua. Quis ipsum suspendisse ultrices gravida. Risus commodo viverra maecenas accumsan lacus vel facilisis.</p>
    <p>Lorem ipsum dolor sit amet, consectetur adipiscing elit, sed do eiusmod tempor incididunt ut labore et dolore magna aliqua. Quis ipsum suspendisse ultrices gravida. Risus commodo viverra maecenas accumsan lacus vel facilisis. Lorem ipsum dolor sit amet, consectetur adipiscing elit, sed do eiusmod tempor incididunt ut labore et dolore magna aliqua. Quis ipsum suspendisse ultrices gravida. Risus commodo viverra maecenas accumsan lacus vel facilisis.</p>
  </div>
  <a class="abs btn btn-small board-btn" href="#">Read more</a>

  <!-- blog -->
  <h2 class="abs display blog-title"><span class="accent">Latest</span> blog posts</h2>
  <div class="abs blog-feature" role="img" aria-label="Photograph of a crowd gathered under a lit entrance canopy at night"></div>

  <div class="abs post-thumb thumb-1" role="img" aria-label="Photograph of people seated at a meeting table"></div>
  <article class="abs post-text" style="top:2578px">
    <div class="post-date">Apr 27 2022</div>
    <h3 class="post-heading">Lorem ipsum dolor sit amet, consectetur adipiscing elit</h3>
    <p class="post-excerpt">Lorem ipsum dolor sit amet, consectetur adip is cing elit, sed do eiusmod tempor incididunt ut labore et dolore magna aliqua. Quis ipsum suspendisse ultrices gravida.</p>
  </article>

  <div class="abs post-thumb thumb-2" role="img" aria-label="Photograph of a pilot and young passenger inside a small aircraft cockpit"></div>
  <article class="abs post-text" style="top:2772px">
    <div class="post-date">Apr 27 2022</div>
    <h3 class="post-heading">Lorem ipsum dolor sit amet, consectetur adipiscing elit</h3>
    <p class="post-excerpt">Lorem ipsum dolor sit amet, consectetur adip is cing elit, sed do eiusmod tempor incididunt ut labore et dolore magna aliqua. Quis ipsum suspendisse ultrices gravida.</p>
  </article>

  <div class="abs post-thumb thumb-3" role="img" aria-label="Photograph of a small jet parked on an airfield apron"></div>
  <article class="abs post-text" style="top:2967px">
    <div class="post-date">Apr 27 2022</div>
    <h3 class="post-heading">Lorem ipsum dolor sit amet, consectetur adipiscing elit</h3>
    <p class="post-excerpt">Lorem ipsum dolor sit amet, consectetur adip is cing elit, sed do eiusmod tempor incididunt ut labore et dolore magna aliqua. Quis ipsum suspendisse ultrices gravida.</p>
  </article>

  <!-- footer -->
  <svg class="abs footer-shape" width="1200" height="528" viewBox="0 0 1200 528" aria-hidden="true">
    <defs>
      <linearGradient id="footFill" x1="0" y1="0" x2="0" y2="1">
        <stop offset="0" stop-color="#e9e8ea"/>
        <stop offset="1" stop-color="#f6f5f6"/>
      </linearGradient>
    </defs>
    <rect width="1200" height="528" fill="url(#footFill)"/>
    <path d="M0 0 H1200 V150 C1150 120 1100 110 1060 115 C900 140 700 170 480 160 C250 150 90 80 0 30 Z" fill="#fff"/>
    <path d="M0 30 C90 80 250 150 480 160 C700 170 900 140 1060 115 C1100 110 1150 120 1200 150 L1200 210 C1150 150 1100 140 1060 140 C900 160 700 195 480 190 C250 185 70 120 0 65 Z" fill="var(--red)"/>
  </svg>
  <svg class="abs badge" width="238" height="238" viewBox="0 0 238 238" aria-hidden="true">
    <circle cx="119" cy="119" r="117" fill="#fff" stroke="var(--red-dark)" stroke-width="4"/>
    <circle cx="119" cy="119" r="82" fill="var(--red)"/>
  </svg>

  <div class="abs brand brand-footer"><div class="line1">DALWORTH</div><div class="line2">FOR KIVA</div></div>

  <nav class="abs nav nav-footer">
    <a class="active" href="#">Home</a>
    <a href="#">KIVA Board</a>
    <a href="#">Automotive</a>
    <a href="#">Aviation</a>
    <a href="#">Other Experiences</a>
    <a href="#">Photos</a>
  </nav>

  <div class="abs contact-pill">
    <span><svg width="15" height="11" viewBox="0 0 15 11"><rect width="15" height="11" rx="1" fill="var(--red)"/><path d="M0 1 L7.5 6.5 L15 1" stroke="#fff" stroke-width="1.5" fill="none"/></svg>alex.dalworth@northmarkdx.com</span>
    <span><svg width="14" height="14" viewBox="0 0 24 24"><path d="M6.6 10.8a15 15 0 0 0 6.6 6.6l2.2-2.2a1 1 0 0 1 1-.3 11 11 0 0 0 3.6.6 1 1 0 0 1 1 1V20a1 1 0 0 1-1 1A17 17 0 0 1 3 4a1 1 0 0 1 1-1h3.5a1 1 0 0 1 1 1 11 11 0 0 0 .6 3.6 1 1 0 0 1-.3 1Z" fill="var(--red)"/></svg>Phone: (555)XXX-XXXX</span>
  </div>

  <p class="abs copyright">©2022 dalworth4kiva.com. &nbsp;All Rights Reserved.</p>
</div>
</body>
</html>
```